Birchwell Craft House business card design- Fine Art sculpture business (Contract guaranteed)

This business card is for a fine art business. Though we don't have a website up and running yet it should be up soon. I would like the business card to be elegant and fairly simple with a picture of one of my sculptures on the front (you might need to photoshop out the background) as well as my basic contact info (my name,phone # and e-mail). On the back I'd like it to be pretty simple with just "Notes" and some blank lines for writing in info.
Updates

Target Market(s)

High end artwork buyers

Industry/Entity Type

Art Gallery

Contact Information for Business Card

Wendell Marsh Phone: (555) 312-4098 E-mail: wendell@quarrymint.example Facebook: @birchwellcrafthouse Instagram: birchwellcrafthouse

Colors

Designer to choose colors to be used in the design.

Requirements
Must have
• *A picture of one of my sculptures*, my name, business name (Birchwell Craft House), e-mail, phone #, and a notes section on the back.
• Birchwell Craft House
• Wendell Marsh
• (555)312-4098
• wendell@quarrymint.example
• Facebook: @birchwellcrafthouse
• Instagram: birchwellcrafthouse
Nice to have
• It'd be nice if you can crop out the background in the sculpture pictures, which ever one you end up using.

```html
<!DOCTYPE html>
<html lang="en">
<head>
<meta charset="utf-8">
<title>Birchwell Craft House – Business Card</title>
<link rel="stylesheet" href="https://fonts.googleapis.com/css2?family=Cormorant+Garamond:wght@500&family=Figtree:wght@500&display=swap">
<style>
  :root {
    --page: #ffffff;
    --card-black: #000000;
    --card-white: #ffffff;
    --brand-beige: #cfc6a2;
    --notes-plum: #5e1446;
    --rule-grey: #9a9a9a;
    --contact-white: #ffffff;
    --amethyst-deep: #2a0d4a;
    --amethyst-mid: #5a2a9a;
    --amethyst-light: #8a55d0;
    --granite: #6b6b66;
  }
  * { margin: 0; padding: 0; box-sizing: border-box; }
  html, body { width: 1200px; height: 1000px; overflow: hidden; background: var(--page); }
  .canvas { position: relative; width: 1200px; height: 1000px; }

  .card {
    position: absolute; top: 60px; height: 840px;
    box-shadow: 6px 6px 10px rgba(0,0,0,0.45);
    overflow: hidden;
  }

  /* Front */
  .card--front { left: 64px; width: 511px; background: var(--card-black); }
  .sculpture-photo {
    position: absolute; left: 0; top: 0; width: 275px; height: 100%;
    background:
      radial-gradient(ellipse 70% 25% at 40% 96%, var(--granite) 0%, rgba(0,0,0,0) 100%),
      radial-gradient(ellipse 80% 30% at 45% 20%, var(--amethyst-light) 0%, var(--amethyst-mid) 40%, var(--amethyst-deep) 75%, rgba(0,0,0,0) 100%),
      radial-gradient(ellipse 70% 22% at 30% 77%, var(--amethyst-light) 0%, var(--amethyst-mid) 45%, var(--amethyst-deep) 80%, rgba(0,0,0,0) 100%),
      var(--card-black);
  }
  .front-brand {
    position: absolute; right: 42px; top: 470px; text-align: right;
    font-family: "Cormorant Garamond", serif; font-weight: 500;
    color: var(--brand-beige); line-height: 1.05;
  }
  .front-brand__line { display: block; font-size: 56px; }
  .front-brand__line--small { font-size: 40px; letter-spacing: 0.12em; margin-top: 14px; }

  /* Back */
  .card--back { left: 630px; width: 510px; background: var(--card-white); }
  .notes-title {
    position: absolute; left: 33px; top: 40px;
    font-family: "Cormorant Garamond", serif; font-weight: 500;
    font-size: 40px; letter-spacing: 0.08em; color: var(--notes-plum);
  }
  .notes-lines { position: absolute; left: 0; top: 0; }
  .contact-band {
    position: absolute; left: 0; top: 597px; width: 100%; height: 243px;
    background: var(--card-black);
  }
  .back-brand {
    position: absolute; right: 40px; top: 22px; text-align: right;
    font-family: "Cormorant Garamond", serif; font-weight: 500;
    color: var(--brand-beige); font-size: 30px; line-height: 1.1;
  }
  .back-brand__line { display: block; }
  .back-brand__line--small { font-size: 20px; letter-spacing: 0.12em; }
  .contact-list {
    position: absolute; left: 33px; top: 120px; list-style: none;
    font-family: "Figtree", sans-serif; font-weight: 500;
    font-size: 26px; line-height: 34px; color: var(--contact-white);
  }
</style>
</head>
<body>
<main class="canvas">
  <section class="card card--front">
    <div class="sculpture-photo" role="img" aria-label="Photograph of an amethyst geode sculpture with purple crystals, pinched at the middle, standing on a round granite base"></div>
    <div class="front-brand">
      <span class="front-brand__line">Birchwell</span>
      <span class="front-brand__line front-brand__line--small">CRAFT HOUSE</span>
    </div>
  </section>

  <section class="card card--back">
    <h2 class="notes-title">notes:</h2>
    <svg class="notes-lines" width="510" height="597" aria-hidden="true">
      <g stroke="var(--rule-grey)" stroke-width="4" stroke-linecap="round" stroke-dasharray="0 11">
        <line x1="36" y1="137" x2="472" y2="137"/>
        <line x1="36" y1="204" x2="472" y2="204"/>
        <line x1="36" y1="271" x2="472" y2="271"/>
        <line x1="36" y1="337" x2="472" y2="337"/>
        <line x1="36" y1="404" x2="472" y2="404"/>
        <line x1="36" y1="471" x2="472" y2="471"/>
        <line x1="36" y1="538" x2="472" y2="538"/>
      </g>
    </svg>
    <div class="contact-band">
      <div class="back-brand">
        <span class="back-brand__line">Birchwell</span>
        <span class="back-brand__line back-brand__line--small">CRAFT HOUSE</span>
      </div>
      <ul class="contact-list">
        <li>Wendell Marsh</li>
        <li>(555) 312-4098</li>
        <li>wendell@quarrymint.example</li>
      </ul>
    </div>
  </section>
</main>
</body>
</html>
```